Dorian Blakely & Morning Lanterns

I need a cd cover designed for a Gospel/Christian Choir. I'm attaching the main picture I want on the cover. This is our single "Lift my heart higher".

Requirements
Must have
• Single name: Lift My Heart Higher

```html
<!DOCTYPE html>
<html lang="en">
<head>
<meta charset="utf-8">
<title>Dorian Blakely &amp; Morning Lanterns — Lift My Heart Higher</title>
<link href="https://fonts.googleapis.com/css2?family=Inter:ital,wght@0,300;0,900;1,300&family=Playfair+Display:wght@700&display=swap" rel="stylesheet">
<style>
  :root {
    --night: #0b1526;
    --navy: #13243d;
    --ember: #b8481a;
    --amber: #e98a3a;
    --gold: #ddb01c;
    --white: #ffffff;
    --band: rgba(150, 150, 150, 0.55);
  }
  html, body {
    margin: 0;
    padding: 0;
    width: 1200px;
    height: 1200px;
    overflow: hidden;
    background: var(--night);
  }
  .cover {
    position: relative;
    width: 1200px;
    height: 1200px;
    overflow: hidden;
  }
  .cover-photo {
    position: absolute;
    inset: 0;
    display: block;
  }
  .artist {
    position: absolute;
    left: 58px;
    top: 48px;
    margin: 0;
    color: var(--white);
    font-family: "Inter", sans-serif;
    line-height: 0.98;
  }
  .artist-lead {
    display: block;
    font-weight: 900;
    font-size: 74px;
    letter-spacing: 0.01em;
  }
  .artist-amp {
    font-weight: 300;
    font-size: 70px;
  }
  .artist-group {
    display: block;
    font-weight: 300;
    font-style: italic;
    font-size: 76px;
    margin-top: 4px;
  }
  .single-title {
    position: absolute;
    left: 112px;
    top: 850px;
    margin: 0;
    font-family: "Playfair Display", serif;
    font-weight: 700;
    line-height: 1;
  }
  .title-top {
    display: block;
    color: var(--gold);
    font-size: 96px;
    letter-spacing: 0.02em;
  }
  .title-bottom {
    display: block;
    color: var(--white);
    font-size: 90px;
    letter-spacing: 0.34em;
    margin-top: 12px;
  }
  .title-band {
    position: absolute;
    left: 0;
    top: 1079px;
    width: 1200px;
    height: 56px;
    background: linear-gradient(90deg, rgba(150,150,150,0.15) 0%, var(--band) 35%, var(--band) 100%);
  }
</style>
</head>
<body>
  <main class="cover">
    <svg class="cover-photo" role="img" aria-label="Photograph of the lead singer in a satin suit and patterned tie, leaning against a warmly lit building at night with blurred street lights" width="1200" height="1200" viewBox="0 0 1200 1200">
      <defs>
        <linearGradient id="scene" x1="0" y1="0" x2="1" y2="0.3">
          <stop offset="0" stop-color="#0d1a2e"/>
          <stop offset="0.35" stop-color="#1d2230"/>
          <stop offset="0.65" stop-color="#6a2a14"/>
          <stop offset="0.85" stop-color="#b8481a"/>
          <stop offset="1" stop-color="#e98a3a"/>
        </linearGradient>
        <linearGradient id="suit" x1="0" y1="0" x2="0" y2="1">
          <stop offset="0" stop-color="rgba(19,36,61,0)"/>
          <stop offset="1" stop-color="rgba(19,36,61,0.9)"/>
        </linearGradient>
      </defs>
      <rect width="1200" height="1200" fill="url(#scene)"/>
      <rect x="0" y="600" width="1200" height="600" fill="url(#suit)"/>
    </svg>

    <h1 class="artist">
      <span class="artist-lead">DORIAN</span>
      <span class="artist-lead">BLAKELY<span class="artist-amp">&amp;</span></span>
      <span class="artist-group">MORNING</span>
      <span class="artist-group">LANTERNS</span>
    </h1>

    <div class="title-band"></div>

    <h2 class="single-title">
      <span class="title-top">LIFT MY HEART</span>
      <span class="title-bottom">HIGHER</span>
    </h2>
  </main>
</body>
</html>
```